Health & Wellness Website

Corvantel focuses on helping people with chronic health conditions through communication, education and behavior management. See the attached summary for more info on the company.

The attached wire frames should be turned into a very intuitive and simple website design. The design should have a minimal, modern, and yet still personal feel since the main point of the site is for people with chronic health conditions to be able to express themselves and find others that are like them.

There are 18 pages in the wire frames, but most of them have very similar content and page layouts. The design of the pages should to be as similar to each other as possible with most of the features and formats being repeated. The layout is not set in stone and the primary focus should be on intuitive use.

There should be two versions of the designs: one for tablets in the portrait mode (768 px) and one in the landscape mode (1024 px). These layouts should be included in the winning design.

If you would like to submit one page, I will check the posting and give feedback frequently so you don't waste your time and have to change everything.

Target Market(s)

The target market for this website has two different groups within the overall chronic health patient umbrella. The primary group are people who are under 55 yrs old and already use one or more social media sites. The other group consists of people that are older and less familiar with modern websites. The site needs to be catered to the latter and be incredibly intuitive.

Industry/Entity Type

Education

Requirements
Must have
• INTUITIVE DESIGN that is simple, minimal, and modern with a limited color palette. Tablet landscape and portrait versions are needed. Adobe Fireworks is the preferred program and will give submitted designs a huge leg up in the decision. Adobe Photoshop is the only other acceptable program to use. The designer will also need to make the social media icons, buttons, and other graphic design items that are needed for to go along with the theme. These should be vector graphics and be created either in Adobe Fireworks or Illustrator. All working files for the pages, icons, and graphics will be required once the winner is chosen.
• The necessary pages include: the landing page (long scrolling page with about and community sections); a general modal pop-up layout that includes forms and text; the template for inside of the members area (Home Page in wire frames); the community page; and the profile page (with tabs). Please include all the pages you feel it takes to communicate your design.
Nice to have
• Descriptions of transition effects and notes for the programmers are a good thing. The designer might consider adding navigation on the public landing page that scrolls with the header (This is not in the wire frames).
Should not have
• Flashy or complex features that require a lot of code to accomplish. Should not look like Plaztera.

```html
<!DOCTYPE html>
<html lang="en">
<head>
<meta charset="utf-8">
<title>Corvantel — Welcome</title>
<link href="https://fonts.googleapis.com/css2?family=Source+Sans+3:wght@400;600&display=swap" rel="stylesheet">
<style>
:root{
  --ink:#4a4a5c;
  --muted:#8b8ba0;
  --slate:#6e6e84;
  --slate-dark:#55556a;
  --card:#f1f1fb;
  --band:#ececee;
  --white:#ffffff;
  --footer-band:#7c7c92;
}
*{box-sizing:border-box;margin:0;padding:0}
html,body{width:1200px;height:978px;overflow:hidden}
body{position:relative;background:var(--white);font-family:"Source Sans 3",sans-serif;color:var(--ink)}
.top-band{position:absolute;left:0;top:0;width:1200px;height:323px;background:linear-gradient(#fafafa,var(--band))}
.brand{position:absolute;left:112px;top:28px;width:186px;text-align:center}
.brand-mark{display:block;width:52px;height:52px;margin:0 auto 10px;border-radius:50%;background:var(--slate)}
.brand-name{font-size:22px;font-weight:400;letter-spacing:5px;color:var(--slate)}
.brand-tagline{font-size:11px;color:var(--slate);margin-top:2px}
.search{position:absolute;left:876px;top:43px;width:220px;height:36px;background:var(--white);border:1px solid #d6d6dc;border-radius:5px;font-size:11px;color:#555;padding:12px 16px}
.search svg{position:absolute;right:12px;top:9px}
.btn{position:absolute;display:flex;align-items:center;justify-content:center;color:var(--white);font-size:14px;border-radius:3px;background:linear-gradient(#8a8aa0,var(--slate-dark))}
.btn-login{left:926px;top:98px;width:73px;height:30px}
.btn-signup{left:1006px;top:98px;width:92px;height:30px}
.login-panel{position:absolute;left:907px;top:132px;width:193px;height:141px;background:rgba(90,90,110,.85);border-radius:4px;z-index:2}
.field{position:absolute;left:18px;width:163px;height:31px;background:rgba(180,180,200,.6);border-radius:3px;color:var(--white);font-size:12px;padding:8px 14px}
.field-user{top:14px}.field-pass{top:53px}
.btn-signin{left:45px;top:98px;width:97px;height:31px;background:linear-gradient(#d4d4dc,#9a9aaa);font-size:13px}
.hero{position:absolute;left:101px;top:142px;width:999px;height:422px;border-radius:3px;overflow:hidden;background:linear-gradient(100deg,#6d5a4c 0%,#8f8a84 30%,#5fa7a2 55%,#c8b8a2 75%,#a84a3a 100%)}
.hero-caption{position:absolute;left:555px;top:197px;width:425px;height:196px;background:rgba(40,40,40,.72);border-radius:3px;padding:26px 28px;color:var(--white)}
.hero-caption h1{font-size:42px;font-weight:600;line-height:1}
.hero-caption p{font-size:21px;line-height:24px;margin-top:22px;color:#eee}
.slider-arrow{position:absolute;top:368px;width:29px;height:29px;border-radius:50%;background:#222}
.slider-arrow svg{display:block;margin:8px auto}
.arrow-prev{left:44px}.arrow-next{left:81px}
.intro{position:absolute;left:0;top:589px;width:1200px;text-align:center;font-size:19px;font-weight:600;line-height:26px;color:var(--muted)}
.divider{position:absolute;left:115px;width:975px;height:1px;background:linear-gradient(90deg,transparent,#8a8a96 20%,#8a8a96 80%,transparent)}
.divider-top{top:655px}.divider-bottom{top:880px}
.card{position:absolute;top:680px;width:308px;height:178px;background:var(--card);border-radius:3px;text-align:center}
.card h2{font-size:20px;font-weight:400;margin-top:13px;color:var(--ink)}
.card-icon{position:absolute;left:50%;top:48px;transform:translateX(-50%)}
.card .btn{top:130px;left:50%;transform:translateX(-50%);width:92px;height:31px}
.card-about{left:123px}.card-community{left:445px}.card-signup{left:767px}
.footer-nav{position:absolute;left:137px;top:915px;display:flex;gap:28px;font-size:14px;color:#333;list-style:none}
.social{position:absolute;left:880px;top:898px;display:flex;gap:10px;align-items:center;list-style:none}
.social li{display:flex;align-items:center;gap:4px;font-size:11px;color:var(--slate)}
.social li span{display:block;width:22px;height:22px;border-radius:50%;background:#a8a8b4}
.social li:first-child span{background:var(--slate)}
.copyright{position:absolute;right:139px;top:941px;font-size:12px;color:#333}
.footer-band{position:absolute;left:0;top:968px;width:1200px;height:10px;background:var(--footer-band)}
</style>
</head>
<body>
<div class="top-band"></div>

<header class="brand">
  <span class="brand-mark"></span>
  <div class="brand-name">CORVANTEL</div>
  <div class="brand-tagline">Persistm, Share, and Prosper</div>
</header>

<div class="search">Search
  <svg width="18" height="18" viewBox="0 0 18 18"><circle cx="7" cy="7" r="5.5" fill="none" stroke="#777" stroke-width="1.6"/><line x1="11" y1="11" x2="16" y2="16" stroke="#777" stroke-width="2.4" stroke-linecap="round"/></svg>
</div>
<div class="btn btn-login">LOGIN</div>
<div class="btn btn-signup">SIGN UP</div>

<form class="login-panel">
  <div class="field field-user">Username</div>
  <div class="field field-pass">Password</div>
  <div class="btn btn-signin">SIGNIN</div>
</form>

<section class="hero" role="img" aria-label="Photo of two students working at a desk with a smiling teacher leaning over them">
  <div class="hero-caption">
    <h1>WELCOME</h1>
    <p>We help people with chronic health conditions through communication, education and behavior management.</p>
  </div>
  <div class="slider-arrow arrow-prev"><svg width="12" height="12" viewBox="0 0 12 12"><path d="M9 1 L3 6 L9 11Z" fill="#fff"/></svg></div>
  <div class="slider-arrow arrow-next"><svg width="12" height="12" viewBox="0 0 12 12"><path d="M3 1 L9 6 L3 11Z" fill="#fff"/></svg></div>
</section>

<p class="intro">Corvantel is an online, community-centric approach to wellness through education,<br>communication, and behavioral management for people with chronic health conditions.</p>
<div class="divider divider-top"></div>

<article class="card card-about">
  <h2>About Corvantel</h2>
  <svg class="card-icon" width="60" height="60" viewBox="0 0 60 60"><circle cx="30" cy="30" r="26" fill="#7c7c92"/></svg>
  <div class="btn">VIEW MORE</div>
</article>
<article class="card card-community">
  <h2>Community Highlights</h2>
  <svg class="card-icon" width="60" height="60" viewBox="0 0 60 60"><rect x="14" y="4" width="32" height="20" rx="6" fill="#7c7c92"/><path d="M24 24 L22 30 L30 24Z" fill="#7c7c92"/><circle cx="23" cy="14" r="2" fill="#f1f1fb"/><circle cx="30" cy="14" r="2" fill="#f1f1fb"/><circle cx="37" cy="14" r="2" fill="#f1f1fb"/><rect x="6" y="36" width="48" height="20" rx="8" fill="#7c7c92"/></svg>
  <div class="btn">VIEW MORE</div>
</article>
<article class="card card-signup">
  <h2>Sign Up</h2>
  <svg class="card-icon" width="60" height="60" viewBox="0 0 60 60"><path d="M30 10 H10 V52 H50 V32" fill="none" stroke="#7c7c92" stroke-width="5"/><path d="M46 4 L56 14 L30 40 L18 44 L22 32Z" fill="#7c7c92"/></svg>
  <div class="btn">VIEW MORE</div>
</article>

<div class="divider divider-bottom"></div>

<ul class="footer-nav">
  <li>Home</li><li>About</li><li>Services</li><li>Contact</li>
</ul>
<ul class="social">
  <li><span></span>Plaztera</li>
  <li><span></span>Linkora</li>
  <li><span></span>Chirpwell</li>
</ul>
<p class="copyright">©&nbsp;2013&nbsp;&nbsp;&nbsp;www.Corvantel.com</p>
<div class="footer-band"></div>
</body>
</html>
```